Symposium Flyer

I need a flyer for advertising an upcoming symposium titled, "Stirring and settling the chromatin map", I am organizing as well as a webpage design for the symposium. The Symposium is taking place on Thursday, February 7th, 2019 at the Halvorsen College Dunmere School of Medicine. It is being held by the Genomic Regulation Collegium at the Vantreck Hall for Applied Discovery (Kellaway Auditorium and Lobby, 2750 Orchard Terrace Way, Philadelphia, PA 19187). You can view previous symposiums from our institution at https://events.hdsm-example.org/genreg/meetings/

Our Keynote speakers for this symposium are:
Ottokar Brummell, M.D., Professor of Biology at the Northvale Polytechnic of Applied Science; Founding Member of the Corriveau Foundation for Life Science Study; Member of the Council of Clinical Scholars.
AND
Thomas (Tom) Weylund, M.D., President of the Lumavex Centers for Therapeutic Discovery (LCTD)

We will be adding 8 more speakers to this event, so please leave room for extra speakers to be added and for a website registration link and QR code to be added.

Please email me should have additional questions - corvi@hdsm-example.org

```html
<!DOCTYPE html>
<html lang="en">
<head>
<meta charset="utf-8">
<title>Stirring and Settling the Chromatin Map — Symposium Flyer</title>
<link rel="stylesheet" href="https://fonts.googleapis.com/css2?family=Barlow:wght@500;600;700;800&family=Tinos:ital,wght@0,400;0,700;1,400&display=swap">
<style>
  :root {
    --page-bg: #e6e7e8;
    --ink-black: #0a0a0a;
    --accent-red: #d7263d;
    --accent-cyan: #4fc6d6;
    --name-blue: #1b6fb6;
    --footer-red: #d62839;
    --rule-blue: #2a76c0;
    --body-ink: #222;
    --white: #ffffff;
  }
  * { box-sizing: border-box; margin: 0; padding: 0; }
  html, body {
    width: 907px; height: 1200px; overflow: hidden;
    background: var(--page-bg);
  }
  .flyer {
    position: absolute; left: 35px; top: 8px;
    width: 836px; height: 1183px;
    background: var(--white);
    overflow: hidden;
    font-family: "Barlow", Arial, sans-serif;
  }
  .header-shape { position: absolute; left: 0; top: 0; width: 836px; height: 600px; }
  .title {
    position: absolute; left: 0; width: 836px; top: 68px;
    text-align: center; color: var(--white);
    font-weight: 800; font-size: 64px; line-height: 70px; letter-spacing: 0.5px;
  }
  .molecule-art {
    position: absolute; left: 31px; top: 252px; width: 355px; height: 265px;
    border-radius: 45% 55% 50% 50%;
    background: radial-gradient(ellipse at 50% 45%, #6b3fa8 0%, #3b3a9a 40%, rgba(60,170,200,0.45) 65%, rgba(10,10,10,0) 75%);
  }
  .info-block {
    position: absolute; left: 422px;
    border-left: 2px solid var(--white);
    padding-left: 16px;
    font-weight: 700;
  }
  .info-date { top: 270px; color: var(--accent-red); font-size: 33px; line-height: 40px; }
  .info-venue { top: 367px; color: var(--accent-cyan); font-size: 32px; line-height: 40px; }

  .speakers { position: absolute; left: 0; top: 560px; width: 836px; height: 453px; }
  .column-shade {
    position: absolute; left: 412px; top: 0; width: 14px; height: 453px;
    background: linear-gradient(to right, rgba(0,0,0,0.10), rgba(0,0,0,0.02) 60%, rgba(0,0,0,0));
  }
  .speaker { position: absolute; width: 350px; }
  .speaker-name {
    display: flex; align-items: center; gap: 10px;
    font-family: "Tinos", "Times New Roman", serif; font-weight: 700;
    color: var(--name-blue); font-size: 18px; line-height: 20px;
  }
  .speaker-name svg { flex: none; margin-left: -28px; }
  .speaker-name { padding-left: 28px; margin-left: -28px; }
  .speaker-role {
    margin-top: 4px;
    font-family: "Tinos", "Times New Roman", serif; font-style: italic;
    color: var(--body-ink); font-size: 9.6px; line-height: 13px;
  }

  .footer-rule { position: absolute; left: 0; top: 1013px; width: 836px; height: 7px; background: var(--rule-blue); }
  .footer {
    position: absolute; left: 0; top: 1020px; width: 836px; height: 163px;
    background: var(--footer-red); color: var(--white);
  }
  .footer-host { position: absolute; left: 71px; top: 14px; font-weight: 600; font-size: 21px; line-height: 28px; }
  .footer-address { position: absolute; left: 71px; top: 80px; font-weight: 500; font-size: 17px; line-height: 23px; }
  .footer-marks { position: absolute; left: 570px; top: 22px; width: 200px; }
  .mark { display: flex; align-items: center; gap: 8px; font-weight: 600; font-size: 15px; line-height: 18px; margin-bottom: 14px; }
  .mark-dot { flex: none; width: 14px; height: 14px; border-radius: 50%; background: var(--white); }
</style>
</head>
<body>
<main class="flyer">
  <svg class="header-shape" viewBox="0 0 836 600" aria-hidden="true">
    <path transform="translate(0,16)" fill="var(--accent-cyan)" d="M0 0 H836 V465 C780 508 700 548 600 560 C420 578 200 548 0 560 Z"/>
    <path transform="translate(0,6)" fill="var(--accent-red)" d="M0 0 H836 V465 C780 508 700 548 600 560 C420 578 200 548 0 560 Z"/>
    <path fill="var(--ink-black)" d="M0 0 H836 V465 C780 508 700 548 600 560 C420 578 200 548 0 560 Z"/>
  </svg>

  <h1 class="title">STIRRING &amp; SETTLING<br>THE CHROMATIN MAP</h1>

  <div class="molecule-art" role="img" aria-label="Illustration of a chromatin protein structure wrapped in glowing cyan DNA strands"></div>

  <p class="info-block info-date">THURSDAY,<br>FEBRUARY 7th 2019</p>
  <p class="info-block info-venue">At Halvorsen College<br>Dunmere School<br>Of Medicine</p>

  <section class="speakers">
    <div class="column-shade"></div>

    <div class="speaker" style="left:99px; top:64px;">
      <p class="speaker-name"><svg width="18" height="18" viewBox="0 0 18 18"><circle cx="9" cy="9" r="9" fill="#c8202f"/><path d="M7 5 L11 9 L7 13" stroke="#fff" stroke-width="2.4" fill="none"/></svg>Ottokar Brummell, M.D.</p>
      <p class="speaker-role" style="margin-left:-28px;">Professor of Biology at the Northvale Polytechnic of Applied Science;<br>Founding Member of the Corriveau Foundation for Life Science Study;<br>Member of the Council of Clinical Scholars.</p>
    </div>
    <div class="speaker" style="left:99px; top:142px;">
      <p class="speaker-name"><svg width="18" height="18" viewBox="0 0 18 18"><circle cx="9" cy="9" r="9" fill="#c8202f"/><path d="M7 5 L11 9 L7 13" stroke="#fff" stroke-width="2.4" fill="none"/></svg>Thomas (Tom) Weylund, M.D.,</p>
      <p class="speaker-role" style="margin-left:-28px;">President of the Lumavex Centers for Therapeutic Discovery (LCTD)</p>
    </div>
    <div class="speaker" style="left:99px; top:194px;">
      <p class="speaker-name"><svg width="18" height="18" viewBox="0 0 18 18"><circle cx="9" cy="9" r="9" fill="#c8202f"/><path d="M7 5 L11 9 L7 13" stroke="#fff" stroke-width="2.4" fill="none"/></svg>Name here name here</p>
      <p class="speaker-role" style="margin-left:-28px;">Professor of Biology at the Northvale Polytechnic of Applied Science;<br>Founding Member of the Corriveau Foundation for Life Science Study;<br>Member of the Council of Clinical Scholars.</p>
    </div>
    <div class="speaker" style="left:99px; top:272px;">
      <p class="speaker-name"><svg width="18" height="18" viewBox="0 0 18 18"><circle cx="9" cy="9" r="9" fill="#c8202f"/><path d="M7 5 L11 9 L7 13" stroke="#fff" stroke-width="2.4" fill="none"/></svg>Name here name here</p>
      <p class="speaker-role" style="margin-left:-28px;">President of the Lumavex Centers for Therapeutic Discovery (LCTD)</p>
    </div>
    <div class="speaker" style="left:99px; top:325px;">
      <p class="speaker-name"><svg width="18" height="18" viewBox="0 0 18 18"><circle cx="9" cy="9" r="9" fill="#c8202f"/><path d="M7 5 L11 9 L7 13" stroke="#fff" stroke-width="2.4" fill="none"/></svg>Name here name here</p>
      <p class="speaker-role" style="margin-left:-28px;">Professor of Biology at the Northvale Polytechnic of Applied Science;<br>Founding Member of the Corriveau Foundation for Life Science Study;<br>Member of the Council of Clinical Scholars.</p>
    </div>

    <div class="speaker" style="left:484px; top:64px;">
      <p class="speaker-name"><svg width="18" height="18" viewBox="0 0 18 18"><circle cx="9" cy="9" r="9" fill="#c8202f"/><path d="M7 5 L11 9 L7 13" stroke="#fff" stroke-width="2.4" fill="none"/></svg>Name here name here</p>
      <p class="speaker-role" style="margin-left:-28px;">President of the Lumavex Centers for Therapeutic Discovery (LCTD)</p>
    </div>
    <div class="speaker" style="left:484px; top:127px;">
      <p class="speaker-name"><svg width="18" height="18" viewBox="0 0 18 18"><circle cx="9" cy="9" r="9" fill="#c8202f"/><path d="M7 5 L11 9 L7 13" stroke="#fff" stroke-width="2.4" fill="none"/></svg>Name here name here</p>
      <p class="speaker-role" style="margin-left:-28px;">Professor of Biology at the Northvale Polytechnic of Applied Science;<br>Founding Member of the Corriveau Foundation for Life Science Study;<br>Member of the Council of Clinical Scholars.</p>
    </div>
    <div class="speaker" style="left:484px; top:205px;">
      <p class="speaker-name"><svg width="18" height="18" viewBox="0 0 18 18"><circle cx="9" cy="9" r="9" fill="#c8202f"/><path d="M7 5 L11 9 L7 13" stroke="#fff" stroke-width="2.4" fill="none"/></svg>Name here name here</p>
      <p class="speaker-role" style="margin-left:-28px;">President of the Lumavex Centers for Therapeutic Discovery (LCTD)</p>
    </div>
    <div class="speaker" style="left:484px; top:257px;">
      <p class="speaker-name"><svg width="18" height="18" viewBox="0 0 18 18"><circle cx="9" cy="9" r="9" fill="#c8202f"/><path d="M7 5 L11 9 L7 13" stroke="#fff" stroke-width="2.4" fill="none"/></svg>Name here name here</p>
      <p class="speaker-role" style="margin-left:-28px;">Professor of Biology at the Northvale Polytechnic of Applied Science;<br>Founding Member of the Corriveau Foundation for Life Science Study;<br>Member of the Council of Clinical Scholars.</p>
    </div>
    <div class="speaker" style="left:484px; top:335px;">
      <p class="speaker-name"><svg width="18" height="18" viewBox="0 0 18 18"><circle cx="9" cy="9" r="9" fill="#c8202f"/><path d="M7 5 L11 9 L7 13" stroke="#fff" stroke-width="2.4" fill="none"/></svg>Name here name here</p>
      <p class="speaker-role" style="margin-left:-28px;">President of the Lumavex Centers for Therapeutic Discovery (LCTD)</p>
    </div>
  </section>

  <div class="footer-rule"></div>
  <footer class="footer">
    <p class="footer-host">Genomic Regulation Collegium At The Vantreck<br>Hall For Applied Discovery</p>
    <p class="footer-address">(Kellaway Auditorium And Lobby,<br>2750 Orchard Terrace Way, Philadelphia, Pa 19187).</p>
    <div class="footer-marks">
      <p class="mark"><span class="mark-dot"></span>Genomic Regulation Collegium</p>
      <p class="mark">Halvorsen College Dunmere School of Medicine</p>
    </div>
  </footer>
</main>
</body>
</html>
```